Vantor Allied Business Card Design

I need a business card design for a renamed company. The company is Vantor Allied.

The design concept is to communicate clean simplicity, clarity, professionalism but also a touch of innovation. That is also our company concept.

** Please note: I've attached my initial design for your review. You don't have to follow that exactly, but I do want you to see what I'm thinking.

Also, I've attached our logo but it's in a format that's probably not good enough for the final product. I can send an updated one later, but this can get you going....

Target Market(s)

CEOs, CFOs, Vice Presidents of Supply Chain, Surgeons

Industry/Entity Type

Business

Requirements
Must have
• White background
• Use font that complements or is similar to our logo
• Minimal type on the front - just the basics
• Use colors: PMS 186 Red, PMS 430 Gray, and PMS 296 Blue
• Back side should be in the Gray or Blue color above - I'm open to which one. But if it's the Gray color it may accommodate someone writing on it better....
Nice to have
• Rounded edges (or some way to add extra or unexpected detail
• Satin-type finish - communicates quality

```html
<!DOCTYPE html>
<html lang="en">
<head>
<meta charset="utf-8">
<title>Vantor Allied Business Card</title>
<link rel="stylesheet" href="https://fonts.googleapis.com/css2?family=Open+Sans:ital,wght@0,400;0,600;1,400&display=swap">
<style>
  :root {
    --brand-blue: #1f4a8c;
    --brand-blue-deep: #17386e;
    --brand-gray: #8e9aa3;
    --brand-red: #d9262f;
    --ink: #333b45;
    --paper: #ffffff;
    --stage: #e9ecef;
  }
  * { box-sizing: border-box; margin: 0; padding: 0; }
  html, body { width: 1200px; height: 840px; overflow: hidden; }
  body {
    background: var(--stage);
    font-family: "Open Sans", sans-serif;
    display: flex;
    align-items: center;
    justify-content: center;
    gap: 40px;
  }
  .card {
    position: relative;
    width: 540px;
    height: 309px;
    border-radius: 10px;
    overflow: hidden;
    box-shadow: 0 4px 14px rgba(0,0,0,.15);
  }

  /* Front */
  .card--front { background: var(--paper); color: var(--ink); }
  .wordmark {
    position: absolute;
    top: 58px; left: 0; right: 0;
    text-align: center;
    font-size: 44px;
    font-weight: 600;
    letter-spacing: -0.5px;
    color: var(--brand-blue);
  }
  .wordmark__dot {
    display: inline-block;
    width: 11px; height: 11px;
    background: var(--brand-red);
    margin-right: 10px;
    vertical-align: 22px;
  }
  .contact {
    position: absolute;
    top: 140px; left: 40px;
    font-size: 13px;
    line-height: 1.45;
  }
  .contact__marker {
    position: absolute;
    top: 142px; left: 0;
    width: 20px; height: 32px;
    background: var(--brand-blue);
  }
  .contact__marker::after {
    content: "";
    position: absolute;
    left: 20px; top: 0;
    width: 8px; height: 32px;
    background: #c9cfd4;
  }
  .contact__name { font-size: 18px; color: var(--brand-blue); line-height: 1.1; }
  .contact__title { font-size: 11px; margin-bottom: 4px; }
  .line { display: flex; align-items: center; gap: 6px; }
  .line svg { width: 11px; height: 11px; fill: var(--brand-blue); flex: none; }
  .divider {
    position: absolute;
    left: 282px; top: 158px;
    width: 1px; height: 82px;
    background: linear-gradient(transparent, #9aa3ab, transparent);
    transform: rotate(18deg);
  }
  .address {
    position: absolute;
    top: 182px; left: 315px;
    font-size: 13px;
    line-height: 1.4;
  }
  .address__indent { padding-left: 17px; }
  .band-rule {
    position: absolute;
    left: 0; right: 0; bottom: 42px;
    height: 4px;
    background: var(--brand-gray);
  }
  .band {
    position: absolute;
    left: 0; right: 0; bottom: 0;
    height: 38px;
    background: var(--brand-blue);
    color: #fff;
    font-style: italic;
    font-size: 13px;
    display: flex; align-items: center; justify-content: center;
  }

  /* Back */
  .card--back {
    background: radial-gradient(ellipse at 40% 30%, #2a5ba0 0%, var(--brand-blue) 45%, var(--brand-blue-deep) 100%);
    color: #fff;
  }
  .back-arcs { position: absolute; inset: 0; width: 100%; height: 100%; }
  .back-content {
    position: absolute; inset: 0;
    display: flex; flex-direction: column;
    align-items: center; justify-content: center;
    gap: 22px;
  }
  .back-content .wordmark {
    position: static;
    color: #fff;
  }
  .back-web { font-size: 13px; letter-spacing: 1px; color: #c9d3e0; }
</style>
</head>
<body>

<section class="card card--front" aria-label="Business card front">
  <div class="wordmark"><span class="wordmark__dot"></span>Vantor Allied</div>

  <div class="contact__marker"></div>
  <div class="contact">
    <div class="contact__name">Dana Whitfield</div>
    <div class="contact__title">VP and Lead Partner</div>
    <div class="line"><svg viewBox="0 0 24 24"><path d="M6.6 10.8a15 15 0 0 0 6.6 6.6l2.2-2.2a1 1 0 0 1 1-.25 11 11 0 0 0 3.6.6 1 1 0 0 1 1 1V20a1 1 0 0 1-1 1A17 17 0 0 1 3 4a1 1 0 0 1 1-1h3.5a1 1 0 0 1 1 1c0 1.25.2 2.45.6 3.6a1 1 0 0 1-.25 1z"/></svg>555.014.2876</div>
    <div class="line"><svg viewBox="0 0 24 24"><path d="M7 1h10a2 2 0 0 1 2 2v18a2 2 0 0 1-2 2H7a2 2 0 0 1-2-2V3a2 2 0 0 1 2-2zm0 3v14h10V4z"/></svg>1.800.555.0147</div>
    <div class="line"><svg viewBox="0 0 24 24"><path d="M2 5h20v14H2zm2 2v.5l8 5 8-5V7z"/></svg>whitfield@vantorallied.com</div>
  </div>

  <div class="divider"></div>

  <div class="address">
    <div class="line"><svg viewBox="0 0 24 24"><path d="M12 3 2 12h3v8h5v-5h4v5h5v-8h3z"/></svg>4120 Meridian Road</div>
    <div class="address__indent">Harlow TN 38099</div>
    <div class="line"><svg viewBox="0 0 24 24"><circle cx="12" cy="12" r="10"/></svg>www.vantorallied.com</div>
  </div>

  <div class="band-rule"></div>
  <div class="band">“Advancing Clinical Results With Less Waste”</div>
</section>

<section class="card card--back" aria-label="Business card back">
  <svg class="back-arcs" viewBox="0 0 540 309" preserveAspectRatio="none" aria-hidden="true">
    <path d="M-40 320 Q 120 60 420 -20" fill="none" stroke="rgba(255,255,255,.06)" stroke-width="60"/>
    <path d="M380 330 Q 560 200 520 -20" fill="none" stroke="rgba(255,255,255,.05)" stroke-width="40"/>
  </svg>
  <div class="back-content">
    <div class="wordmark"><span class="wordmark__dot"></span>Vantor Allied</div>
    <div class="back-web">www.vantorallied.com</div>
  </div>
</section>

</body>
</html>
```